Price list for young Relaxon clinic

I require a price list/Treatment menu for clinic

To include:
Logo
Address
Phone number
Website

List of services and Prices
Relaxon 1 area £100
Relaxon 2 areas £150
Relaxon 3 areas £200
Lip Enhancement 0.5ml £100
Lip Enhancement 1ml £200
Facial Fillers £200 per 1ml
Volumiq £450 per session (2 vials - must be bought as a course)
Non Surgical Face Lift (Thread Lift) £600 per area
Skin Press Full Face £250
Skin Press Small Per Small Area £100
Cryo Therapy £60
Chemical Peel Light Peel and Microdermabrasion £85
Chemical Peel Deep Peel £150
Consultation £30 redeemable against service
Relaxon Top Up Relaxon £50 (must be within 2 weeks of 1st treatment)
Filler Top Up £100 (must be within 2 weeks of 1st appointment)

Open Hours
Updates

Company Name: HVM Address: 482 Pellbrook Road, 6 Warnford High Street, KT4 3JQ Phone: 0208 947 2186 Website: www.hollyvanmereaesthetics.co.uk

Please add more colour

Needs to be much cleaner and simpler Front page to include logo and price list Back page to inculde open hours and contact information including google map. Please no images with needles. Images of lips and faces are good, but try not to crowd copy on the pagei. No copy on top of images. White, grey, black and reds are good on colouring.

Target Market(s)

young market ages 22-45 years old mainly female
modern

Industry/Entity Type

Clinic

Number of Pages Required

4 page

Requirements
Must have
• Logo - logo must be in colour grey/silver
• Address (small map?)
• Phone number
• Web address
• Services
• Open hours
• Prices
• Images

```html
<!DOCTYPE html>
<html lang="en">
<head>
<meta charset="utf-8">
<title>Holly Vanmere Aesthetics – Price List</title>
<link rel="stylesheet" href="https://fonts.googleapis.com/css2?family=Arvo:wght@400;700&display=swap">
<style>
  :root {
    --page-bg: #dfe5e8;
    --paper: #ffffff;
    --footer-bg: #ececec;
    --logo-grey: #7a7a7a;
    --ink: #1b1b1b;
    --teal: #14a3ad;
    --black: #1a1a1a;
    --red: #e43d5a;
    --navy: #1c4470;
    --plum: #9c3b7c;
    --mustard: #c9b00f;
    --photo-a: #efe3d6;
    --photo-b: #cfa98c;
    --map-a: #ecebe6;
    --map-b: #dcdad2;
    --rule: #222222;
  }
  * { box-sizing: border-box; margin: 0; padding: 0; }
  html, body { width: 1046px; height: 1200px; overflow: hidden; }
  body {
    background: var(--page-bg);
    font-family: "Arvo", Georgia, serif;
    color: var(--ink);
  }
  .flyer {
    position: absolute;
    left: 123px; top: 20px;
    width: 800px; height: 1160px;
    background: var(--paper);
    overflow: hidden;
  }
  .brand {
    position: absolute; left: 60px; top: 70px; width: 360px;
    display: flex; flex-direction: column; align-items: center; gap: 22px;
  }
  .brand-mark {
    width: 120px; height: 120px; border-radius: 50%;
    background: var(--logo-grey);
  }
  .brand-name {
    color: var(--logo-grey); font-weight: 400;
    font-size: 30px; line-height: 1.05; letter-spacing: 3px;
    text-align: center; text-transform: uppercase;
  }
  .hero-photo {
    position: absolute; right: 0; top: 0; width: 350px; height: 340px;
    background: radial-gradient(ellipse at 55% 45%, var(--photo-a) 0%, var(--photo-b) 100%);
  }
  .services-title {
    position: absolute; left: 50px; top: 272px;
    font-size: 50px; font-weight: 700; letter-spacing: 1px; line-height: 1;
  }
  .services-title .accent { color: var(--teal); }
  .price-list { position: absolute; left: 0; top: 340px; width: 640px; list-style: none; }
  .price-band {
    height: 55px; padding: 0 30px;
    display: flex; align-items: center; gap: 26px;
    color: #fff; font-size: 17px; line-height: 1.3;
  }
  .price-band--tall { height: 140px; flex-direction: column; align-items: flex-start; justify-content: center; gap: 2px; }
  .price-band--two-line span { max-width: 240px; }
  .band-teal { background: var(--teal); }
  .band-black { background: var(--black); }
  .band-red { background: var(--red); }
  .band-navy { background: var(--navy); }
  .band-plum { background: var(--plum); }
  .band-mustard { background: var(--mustard); }
  .location-map {
    position: absolute; left: 640px; top: 340px; width: 160px; height: 580px;
    background: linear-gradient(160deg, var(--map-a) 0%, var(--map-b) 100%);
  }
  .contact-footer {
    position: absolute; left: 0; top: 920px; width: 800px; height: 240px;
    background: var(--footer-bg);
    display: flex; padding: 40px 50px 0;
  }
  .opening-hours { width: 380px; }
  .opening-hours h2 {
    display: flex; align-items: center; gap: 12px;
    font-size: 24px; font-weight: 400; text-transform: uppercase; margin-bottom: 18px;
  }
  .hours-grid { display: grid; grid-template-columns: 190px 170px; font-size: 14px; line-height: 1.45; }
  .hours-note { font-size: 13px; }
  .divider { width: 1px; height: 150px; background: var(--rule); margin: 0 28px; }
  .contact-list { list-style: none; display: flex; flex-direction: column; gap: 18px; }
  .contact-list li { display: flex; align-items: center; gap: 14px; font-size: 15px; line-height: 1.3; }
  .contact-list .phone { font-size: 24px; }
  .icon { flex: none; }
</style>
</head>
<body>
<main class="flyer">
  <header class="brand">
    <div class="brand-mark" aria-hidden="true"></div>
    <p class="brand-name">Holly Vanmere<br>Aesthetics</p>
  </header>

  <div class="hero-photo" role="img" aria-label="Portrait photograph of a young blonde woman with hands framing her face"></div>

  <h1 class="services-title"><span class="accent">OUR</span> SERVICES</h1>

  <ul class="price-list">
    <li class="price-band band-teal"><span>Relaxon 1 area £100</span><span>Relaxon 2 areas £150</span><span>Relaxon 3 areas £200</span></li>
    <li class="price-band band-black"><span>Lip Enhancement 0.5ml £100</span><span>Lip Enhancement 1ml £200</span></li>
    <li class="price-band band-red"><span>Facial Fillers £200 per 1ml</span></li>
    <li class="price-band band-navy"><span>Volumiq £450 per session (2 vials - must be bought as a course)</span></li>
    <li class="price-band band-teal"><span>Non Surgical Face Lift (Thread Lift) £600 per area</span></li>
    <li class="price-band band-plum"><span>Skin Press Full Face £250</span><span>Skin Press Small Per Small Area £100</span></li>
    <li class="price-band band-mustard"><span>Cryo Therapy £60</span></li>
    <li class="price-band band-teal price-band--two-line"><span>Chemical Peel Light Peel and Microdermabrasion £85</span><span>Chemical Peel Deep Peel £150</span></li>
    <li class="price-band band-red price-band--tall">
      <span>Consultation £30 redeemable against service</span>
      <span>Relaxon Top Up Relaxon £50 (must be within 2 weeks of 1st treatment)</span>
      <span>Filler Top Up £100 (must be within 2 weeks of 1st appointment)</span>
    </li>
  </ul>

  <div class="location-map" role="img" aria-label="Street map showing the clinic location"></div>

  <footer class="contact-footer">
    <section class="opening-hours">
      <h2>
        <svg class="icon" width="24" height="26" viewBox="0 0 24 26" aria-hidden="true">
          <rect x="1.5" y="4" width="21" height="20.5" rx="2" fill="none" stroke="var(--teal)" stroke-width="2.5"/>
          <rect x="1.5" y="4" width="21" height="6" fill="var(--teal)"/>
          <rect x="6" y="1" width="2.5" height="6" fill="var(--teal)"/>
          <rect x="15.5" y="1" width="2.5" height="6" fill="var(--teal)"/>
        </svg>
        Opening Hours
      </h2>
      <div class="hours-grid">
        <div>Monday ..... 10am-4pm<br>Tuesday ..... 10am-4pm<br>Wednesday ..... 12pm-8pm<br>Thursday ..... 7:30am-4:30pm<br><span class="hours-note">(at number 1 Marlowe Street only)</span></div>
        <div>Friday ..... 10am-2pm<br>Saturday ..... 9am-2pm<br>Sunday ..... Closed</div>
      </div>
    </section>
    <div class="divider" aria-hidden="true"></div>
    <ul class="contact-list">
      <li>
        <svg class="icon" width="20" height="28" viewBox="0 0 20 28" aria-hidden="true">
          <path d="M10 1C5 1 1.5 4.6 1.5 9.3 1.5 15.5 10 26 10 26s8.5-10.5 8.5-16.7C18.5 4.6 15 1 10 1z" fill="var(--teal)"/>
          <circle cx="10" cy="9.5" r="3.3" fill="#fff"/>
        </svg>
        <span>482 Pellbrook Road, 6 Warnford High<br>Street, KT4 3JQ</span>
      </li>
      <li class="phone">
        <svg class="icon" width="24" height="24" viewBox="0 0 24 24" aria-hidden="true">
          <path d="M6.5 2.5l3 4-2 2.5c1.2 2.6 3.4 4.8 6 6l2.5-2 4 3-2 4.5C10 20 4 14 2 4.5z" fill="var(--teal)"/>
        </svg>
        <span>0208 947 2186</span>
      </li>
      <li>
        <svg class="icon" width="22" height="22" viewBox="0 0 22 22" aria-hidden="true">
          <g fill="none" stroke="var(--teal)" stroke-width="1.8">
            <circle cx="11" cy="11" r="9.5"/>
            <ellipse cx="11" cy="11" rx="4.2" ry="9.5"/>
            <line x1="1.5" y1="11" x2="20.5" y2="11"/>
          </g>
        </svg>
        <span>www.hollyvanmereaesthetics.co.uk</span>
      </li>
    </ul>
  </footer>
</main>
</body>
</html>
```